SUMMIT GATHERING 2021. August 20th -22nd.

The Hosts of the conference: Grace Tabernacle-Pastors Ron n Della ( Picture with two persons)

Guest Minister: Bishop Lucinda Okotieno. (Cedar Ridge Awakening)

Venue:
Sealand Gateway Lodgeview. 4817 North 239th Avenue Seattle, WA 98174.

Conference times.
Friday August 20th 6pm-8:30pm
Saturday August 21st. 6pm-8:30pm

Sunday August 22nd 10am-1pm
“ CHURCH RENEWAL GATHERING”

5pm-7:30pm
TWOFOLD SURGE GATHERING.

Target Market(s)

18-55

Industry/Entity Type

Religious/ Entertainment.

Requirements
Must have
• A highlight of the Relaunch service on Sunday August 22nd 5pm-7:30pm.
Nice to have
• Excellent ideas….

```html
<!DOCTYPE html>
<html lang="en">
<head>
<meta charset="utf-8">
<title>Summit Gathering 2021 — Grace Tabernacle</title>
<link rel="stylesheet" href="https://fonts.googleapis.com/css2?family=Montserrat:ital,wght@0,400;0,600;0,700;0,800;0,900;1,400;1,600&family=Oswald:wght@500;600&family=Playball&display=swap">
<style>
  :root {
    --page: #e9e9ee;
    --gold: #d9b978;
    --gold-deep: #b8925a;
    --cream: #efdcae;
    --indigo: #4a2fa6;
    --magenta: #b3379b;
    --red: #d0121b;
    --dark-red: #8c1010;
    --ink: #1f1d24;
    --white: #ffffff;
  }
  * { margin: 0; padding: 0; box-sizing: border-box; }
  html, body { width: 1200px; height: 1200px; overflow: hidden; background: var(--page); }
  body { position: relative; font-family: "Montserrat", sans-serif; }

  .flyer { position: absolute; left: 168px; top: 40px; width: 864px; height: 1120px; overflow: hidden; box-shadow: 0 6px 24px rgba(0,0,0,.18); }
  .flyer-art { position: absolute; inset: 0; width: 100%; height: 100%; }
  .t { position: absolute; white-space: nowrap; line-height: 1; }
  .center { transform: translateX(-50%); text-align: center; }

  .brand { left: 124px; top: 112px; color: var(--gold); font-weight: 700; font-size: 17px; letter-spacing: 1px; display: flex; flex-direction: column; align-items: center; gap: 10px; }
  .brand-mark { width: 26px; height: 26px; background: var(--gold); }

  .title-year { left: 576px; top: 38px; font-family: "Oswald", sans-serif; font-weight: 600; font-size: 78px; color: var(--gold); }
  .title-main { left: 580px; top: 112px; font-weight: 900; font-size: 100px; color: var(--white); letter-spacing: -1px; }
  .title-script { left: 585px; top: 190px; font-family: "Playball", cursive; font-size: 82px; color: var(--gold); line-height: 1.05; }

  .days { left: 585px; top: 314px; font-weight: 800; font-size: 23px; color: var(--white); letter-spacing: .5px; }
  .date-pill { position: absolute; left: 383px; top: 348px; width: 397px; height: 62px; border-radius: 31px; background: linear-gradient(180deg, var(--cream), var(--gold)); display: flex; align-items: center; justify-content: center; font-family: "Oswald", sans-serif; font-weight: 600; font-size: 42px; color: var(--dark-red); }
  .evening-time { left: 576px; top: 421px; font-weight: 800; font-size: 24px; color: var(--white); }
  .venue-label { left: 650px; top: 471px; font-weight: 800; font-size: 22px; color: var(--cream); }
  .venue-address { left: 650px; top: 500px; font-size: 18px; color: var(--white); line-height: 1.2; }

  .sunday-banner { position: absolute; left: 0; top: 450px; width: 286px; height: 64px; border-radius: 0 32px 32px 0; background: linear-gradient(180deg, #e3252b, #a90d14); border: 3px solid var(--white); border-left: none; display: flex; align-items: center; padding-left: 22px; font-family: "Oswald", sans-serif; font-weight: 600; font-size: 42px; color: var(--white); }

  .session-time { left: 39px; font-weight: 800; font-size: 24px; color: var(--red); }
  .session-time.morning { top: 533px; }
  .session-time.evening { top: 694px; }
  .session-name { left: 39px; font-weight: 900; font-size: 34px; line-height: 35px; color: var(--indigo); }
  .session-name .accent { color: var(--magenta); }
  .session-name.morning { top: 570px; }
  .session-name.evening { top: 731px; }

  .host-label { left: 689px; top: 786px; font-weight: 900; font-size: 30px; color: var(--red); text-shadow: -2px -2px 0 #fff, 2px -2px 0 #fff, -2px 2px 0 #fff, 2px 2px 0 #fff; }
  .host-church { left: 765px; top: 871px; font-weight: 700; font-size: 15px; color: var(--white); }
  .host-pastors { left: 765px; top: 891px; font-style: italic; font-size: 15px; color: var(--white); }

  .guest-label { left: 414px; top: 990px; font-weight: 900; font-size: 20px; color: var(--white); text-shadow: -1.5px -1.5px 0 var(--gold-deep), 1.5px -1.5px 0 var(--gold-deep), -1.5px 1.5px 0 var(--gold-deep), 1.5px 1.5px 0 var(--gold-deep); }
  .guest-caption { left: 655px; top: 928px; font-size: 15px; color: var(--white); line-height: 1.3; }
  .guest-caption .role { font-style: italic; }
  .guest-caption .ministry { font-weight: 700; }

  .info-label { left: 505px; top: 1040px; font-family: "Playball", cursive; font-size: 21px; color: var(--white); }
  .web-pill { position: absolute; left: 292px; top: 1068px; width: 420px; height: 54px; border-radius: 27px 27px 0 0; background: var(--magenta); border: 4px solid #15131a; border-bottom: none; display: flex; align-items: center; justify-content: center; font-weight: 800; font-size: 17px; color: var(--white); }
</style>
</head>
<body>
<main class="flyer">
  <svg class="flyer-art" viewBox="0 0 665 862" preserveAspectRatio="none" aria-hidden="true">
    <defs>
      <linearGradient id="bg-gradient" x1="0" y1="0" x2="1" y2="1">
        <stop offset="0" stop-color="#3a2db5"/>
        <stop offset=".45" stop-color="#4b3fd0"/>
        <stop offset=".75" stop-color="#8c3cb8"/>
        <stop offset="1" stop-color="#c33d9f"/>
      </linearGradient>
      <linearGradient id="panel-gradient" x1="0" y1="0" x2="1" y2="1">
        <stop offset="0" stop-color="#f1f0f0"/>
        <stop offset="1" stop-color="#cdc6c2"/>
      </linearGradient>
      <linearGradient id="host-photo" x1="0" y1="0" x2="0" y2="1">
        <stop offset="0" stop-color="#2f3fc9"/>
        <stop offset="1" stop-color="#5a3f7a"/>
      </linearGradient>
      <linearGradient id="guest-photo" x1="0" y1="0" x2="0" y2="1">
        <stop offset="0" stop-color="#e3ece6"/>
        <stop offset="1" stop-color="#9d9a96"/>
      </linearGradient>
    </defs>
    <rect class="bg" width="665" height="862" fill="url(#bg-gradient)"/>
    <polygon class="light-panel" points="0,160 115,160 442,790 0,790" fill="url(#panel-gradient)"/>
    <polygon class="corner-block" points="0,615 92,862 0,862" fill="#4130b8"/>
    <line class="corner-stripe" x1="0" y1="600" x2="78" y2="800" stroke="#b3379b" stroke-width="4"/>
    <line class="gold-rule" x1="345" y1="453" x2="665" y2="655" stroke="#d9b978" stroke-width="3"/>

    <g class="brand-disc">
      <circle cx="80" cy="88" r="160" fill="#ffffff"/>
      <circle cx="80" cy="88" r="152" fill="#c8141b"/>
      <circle cx="80" cy="88" r="145" fill="#2b2a2e"/>
    </g>

    <line class="session-rule" x1="0" y1="430" x2="180" y2="430" stroke="#4a63d6" stroke-width="1.5"/>
    <circle cx="180" cy="430" r="2.5" fill="#4a63d6"/>
    <line class="session-rule" x1="0" y1="555" x2="155" y2="555" stroke="#4a63d6" stroke-width="1.5"/>
    <circle cx="155" cy="555" r="2.5" fill="#4a63d6"/>

    <g class="host-frame">
      <circle cx="530" cy="536" r="112" fill="#ffffff"/>
      <circle cx="530" cy="536" r="104" fill="#d0121b"/>
      <circle cx="530" cy="536" r="93" fill="url(#host-photo)" role="img" aria-label="Photo of the hosting pastors, Ron and Della"/>
    </g>

    <g class="guest-frame">
      <circle cx="315" cy="690" r="118" fill="none" stroke="#ffffff" stroke-width="2"/>
      <circle cx="315" cy="690" r="93" fill="#ffffff"/>
      <circle cx="315" cy="690" r="88" fill="#d9b978"/>
      <circle cx="315" cy="690" r="80" fill="url(#guest-photo)" role="img" aria-label="Photo of guest minister Bishop Lucinda Okotieno"/>
    </g>

    <polygon class="footer-band" points="40,786 625,786 665,826 665,862 70,862" fill="#1f1d24"/>
    <line class="footer-rule" x1="40" y1="786" x2="625" y2="786" stroke="#d9b978" stroke-width="3"/>
  </svg>

  <div class="t brand center"><span class="brand-mark"></span>GRACE TABERNACLE</div>

  <h1>
    <span class="t title-year center">2021</span>
    <span class="t title-main center">SUMMIT</span>
    <span class="t title-script center">Gathering</span>
  </h1>

  <p class="t days center">FRIDAY - SATURDAY</p>
  <p class="date-pill">20TH -21ST AUGUST</p>
  <p class="t evening-time center">6 PM - 8:30 PM</p>
  <p class="t venue-label center">VENUE:</p>
  <p class="t venue-address center">Sealand Gateway Lodgeview.<br>4817 North 239th Avenue Seattle, WA 98174.</p>

  <p class="sunday-banner">22ND AUGUST</p>
  <p class="t session-time morning">10 AM - 1 PM</p>
  <p class="t session-name morning">CHURCH<br>RENEWAL<br><span class="accent">GATHERING</span></p>
  <p class="t session-time evening">5 PM - 7:30 PM</p>
  <p class="t session-name evening">TWOFOLD<br>SURGE<br><span class="accent">GATHERING</span></p>

  <p class="t host-label center">HOST</p>
  <p class="t host-church center">GRACE TABERNACLE</p>
  <p class="t host-pastors center">Pastors Ron n Della</p>

  <p class="t guest-label center">GUEST MINISTER</p>
  <p class="t guest-caption center"><span class="role">Bishop</span><br><span class="role">Lucinda Okotieno</span><br><span class="ministry">CEDAR RIDGE</span><br><span class="ministry">AWAKENING</span></p>

  <p class="t info-label center">For More Information:</p>
  <p class="web-pill">WWW.GRACETABERNACLEHUB.COM</p>
</main>
</body>
</html>
```